Facial Tissue Brand Logo and Design

We would like you to design a Logo for the Facial Tissue Brand "Velora" along with the box design. The pack should indicate the pack size (150 x 2 ply). Also our company logo should be present (attached) along with a barcode. The box size dimensions should be 210mm (L) x 110mm (W) x 70mm (H). We are open to all kinds of nice designs which are attractive but not overdone. Happy designing!

UPDATE:
We appreciate the designs so far... but would also love to see more options in a simple and elegent design style that would look good on a table... please see attached below links for reference purpose:

www.pixmarrow.com/image-photo/cleaning-wipes-isolated-on-white-480215736

www.pixmarrow.com/image-photo/cleaning-wipes-isolated-on-white-692048153

www.pixmarrow.com/image-photo/delicate-female-hands-pulling-tissue-out-2875013649

Happy desgining!

We appreciate the designs so far.. but would like to to see some more options.

```html
<!DOCTYPE html>
<html lang="en">
<head>
<meta charset="utf-8">
<title>Velora Facial Tissues – Box Panels</title>
<link rel="stylesheet" href="https://fonts.googleapis.com/css2?family=Allura&family=Caveat:wght@500&family=Montserrat:wght@400;700&display=swap">
<style>
  :root {
    --page: #ffffff;
    --panel: #f4f0fb;
    --panel-edge: #e6e0f2;
    --violet: #6a56b8;
    --violet-deep: #4a3a8f;
    --violet-soft: #a895e0;
    --ink: #3f3a5c;
    --leaf: #6cc24a;
    --leaf-deep: #3f8f2f;
    --brand-blue: #2f6fae;
    --grey: #8a8799;
    --white: #ffffff;
  }
  * { margin: 0; padding: 0; box-sizing: border-box; }
  html, body { width: 1200px; height: 1067px; overflow: hidden; background: var(--page); }
  .canvas { position: relative; width: 1200px; height: 1067px; }

  .panel {
    position: absolute;
    left: 80px;
    width: 1040px;
    background: var(--panel);
    border: 1px solid var(--panel-edge);
  }
  .panel--top { top: 90px; height: 500px; }
  .panel--front { top: 600px; height: 340px; }

  .company {
    position: absolute; left: 60px; top: 50px;
    display: flex; align-items: center; gap: 14px;
  }
  .company__mark { width: 56px; height: 56px; background: var(--brand-blue); }
  .company__name {
    font-family: "Montserrat", sans-serif; font-weight: 400;
    font-size: 22px; line-height: 1.05; color: var(--brand-blue);
    letter-spacing: 1px; text-transform: uppercase;
  }
  .company__country {
    position: absolute; left: 60px; top: 122px;
    font-family: "Montserrat", sans-serif; font-size: 9px;
    letter-spacing: 9px; color: var(--grey); text-transform: uppercase;
  }

  .flowers {
    position: absolute;
    background: radial-gradient(ellipse at 55% 25%, var(--violet-soft) 0%, rgba(168,149,224,0.6) 30%, rgba(108,194,74,0.35) 60%, rgba(244,240,251,0) 78%);
  }
  .panel--top .flowers { left: 60px; top: 180px; width: 420px; height: 320px; }
  .panel--front .flowers { left: 150px; top: 0; width: 300px; height: 340px; }

  .wordmark { position: absolute; text-align: right; }
  .wordmark__name {
    font-family: "Allura", cursive; color: var(--violet);
    display: block; line-height: 1;
  }
  .wordmark__tag {
    font-family: "Caveat", cursive; font-weight: 500; color: var(--violet);
    display: block; line-height: 1;
  }
  .panel--top .wordmark { left: 520px; top: 80px; width: 460px; }
  .panel--top .wordmark__name { font-size: 170px; }
  .panel--top .wordmark__tag { font-size: 44px; margin-top: -30px; }
  .panel--front .wordmark { left: 470px; top: 70px; width: 330px; }
  .panel--front .wordmark__name { font-size: 130px; color: var(--ink); }
  .panel--front .wordmark__tag { font-size: 36px; margin-top: -26px; }

  .badges { position: absolute; left: 540px; top: 360px; display: flex; gap: 40px; }
  .badge {
    width: 140px; height: 80px; border-radius: 50% 46% 50% 48%;
    background: linear-gradient(180deg, var(--violet-soft) 0%, var(--violet) 45%, var(--violet-deep) 85%, var(--leaf) 100%);
    display: flex; flex-direction: column; align-items: center; justify-content: center;
    color: var(--white); font-family: "Montserrat", sans-serif; font-weight: 700;
    text-align: center; line-height: 1.05;
  }
  .badge__big { font-size: 28px; }
  .badge__small { font-size: 13px; letter-spacing: 0.5px; }
  .badge__mid { font-size: 16px; }
  .panel--front .badge { position: absolute; left: 860px; top: 120px; }

  .pack-size {
    position: absolute; left: 860px; top: 220px; width: 140px; text-align: center;
    font-family: "Montserrat", sans-serif; font-size: 16px; color: var(--panel-edge);
  }
</style>
</head>
<body>
<main class="canvas">
  <section class="panel panel--top">
    <div class="company">
      <span class="company__mark"></span>
      <span class="company__name">Norvale<br>Trading FZE</span>
    </div>
    <p class="company__country">United Arab Emirates</p>
    <div class="flowers" role="img" aria-label="Illustration of tall violet flowers on green stems"></div>
    <h1 class="wordmark">
      <span class="wordmark__name">Velora</span>
      <span class="wordmark__tag">facial tissues</span>
    </h1>
    <div class="badges">
      <div class="badge"><span class="badge__big">150</span><span class="badge__small">TISSUES</span></div>
      <div class="badge"><span class="badge__mid">WHITE</span><span class="badge__mid">2 PLY</span></div>
      <div class="badge"><span class="badge__mid">8X7.5</span><span class="badge__mid">INCH</span></div>
    </div>
  </section>

  <section class="panel panel--front">
    <div class="flowers" role="img" aria-label="Illustration of violet flowers on green stems"></div>
    <h2 class="wordmark">
      <span class="wordmark__name">Velora</span>
      <span class="wordmark__tag">facial tissues</span>
    </h2>
    <div class="badge"><span class="badge__big">150</span><span class="badge__small">TISSUES</span></div>
    <p class="pack-size">150 x 2 ply</p>
  </section>
</main>
</body>
</html>
```